Zielgruppe
Bestattungen Angehörige von Verstorbenen
Bestattungshaus Lindmark
Ahornsteig 7
61462 Tannbach
www.bestattungshaus-lindmark.de
info@bestattungshaus-lindmark.de
Tel: 06173 / 4820517
Mobil: 0152 / 83740162 24 Std Erreichbarkeit
Aufgabenstellung
Über mich
Mein Name ist Wolfgang Brenner, ich kann auf eine langjährige Berufserfahrung als Humanbestatter zurückblicken.
Die Versorgung und Bestattung eines Verstobenen, ist für Angehörige ein sehr wichtiger Aspekt.
Daher habe ich es mir zur Aufgabe gemacht, Sie auf diesem Weg in Ruhe und mit Genauigkeit zu begleiten.
Was Sie im Trauerfall beachten müssen
Bitte Bewahren Sie ruhe.
Jeder Trauerfall erfordert gewisse Maßnahmen die man treffen muss da diese im Bestattungsgesetzt Festgehalten sind.
Bitte informieren Sie uns Zeitnah um alles wichtige vorab zu besprechen und den Ablauf der Überführung des Verstorbenen zu klären.
Ein ausführliches Gespräch erfolgt zu einen späteren Zeitpunkt wo alle weiteren Fragen Ihrerseits, der Ablauf der Trauerfeier und oder Beisetzung geplant werden.
Verstirb ein Mensch zuhause
Müssen Sie zunächst den Hausarzt, Hausärztlichenvertretungsdienst (116 117 ),
oder den Rettungsdienst ( 112 ) informieren. Dieser wird dann nach der ersten Leichenschau den Totenschein ausstellen, der für den weiteren Ablauf mit uns sehr wichtig ist.
Tritt der Tod jedoch im Krankenhaus,
Pflege & Altenheim ein kümmert sich die dortige Verwaltung um die Formalitäten.
Unsere Leistungen für Sie
Gerne übernehmen wir für Sie folgende Aufgaben:
Persönliche Beratung und Betreuung Überführung im In- und Ausland
Erledigung sämtlicher Formalitäten (z.B. Todesbescheinigung, Sterbeurkunde.)
Versorgung des Verstorbenen nach DIN EN 15017
Aufbahrung & Abschiednahme in unseren Räumlichkeiten.
Trauerdrucksachen ,Traueranzeigen
Beratung bei der Wahl der Bestattungsform und des Ortes der Beisetzung.
Alle Bestattungsformen und Grab Arten sind bei uns möglich
Terminabsprachen mit Pfarrer/Trauerrednern, Friedhofsverwaltung
Individuelle Gestaltung, Organisation und Betreuung der Trauer P..

```html
<!DOCTYPE html>
<html lang="de">
<head>
<meta charset="utf-8">
<title>Bestattungshaus Lindmark</title>
<link href="https://fonts.googleapis.com/css2?family=Montserrat:wght@400;500&family=Open+Sans:ital,wght@0,400;0,600;0,700;1,400;1,600;1,700&display=swap" rel="stylesheet">
<style>
  :root {
    --ink: #1e1e1e;
    --muted: #6a6a6a;
    --gold: #c9a96a;
    --beige: #e6d3ac;
    --beige-dark: #dcc59a;
    --band: #5f5f5f;
    --footer: #d6d6d6;
    --white: #ffffff;
  }
  * { margin: 0; padding: 0; box-sizing: border-box; }
  html, body { width: 853px; height: 1200px; overflow: hidden; background: var(--white); }
  body { position: relative; font-family: "Open Sans", sans-serif; color: var(--ink); }
  .abs { position: absolute; }

  .footer-band { left: 37px; top: 1050px; width: 780px; height: 98px; background: var(--footer); }
  .main-sheet { left: 37px; top: 480px; width: 780px; height: 596px; background: var(--white); border-radius: 0 0 0 34px; }

  .hero-photo {
    left: 37px; top: 49px; width: 590px; height: 440px;
    background: linear-gradient(90deg, #6d5640 0%, #a08466 30%, #d9cbb8 60%, #f1ece6 85%, #ffffff 100%);
  }
  .hero-fade {
    left: 500px; top: 49px; width: 317px; height: 440px;
    background: linear-gradient(90deg, rgba(255,255,255,0) 0%, #ffffff 45%);
  }
  .logo-shape { left: 37px; top: 49px; }
  .logo-dot { left: 96px; top: 133px; width: 14px; height: 14px; border-radius: 50%; background: var(--muted); }
  .logo-name {
    left: 118px; top: 128px; font-family: "Montserrat", sans-serif; font-weight: 400;
    font-size: 20px; color: var(--muted); line-height: 1.2; white-space: nowrap;
  }

  .title-band { left: 66px; top: 341px; font-family: "Montserrat", sans-serif; font-weight: 500; font-size: 26px; color: var(--white); line-height: 1; }
  .title-band span { display: inline-block; background: var(--band); padding: 6px 6px 8px 7px; margin-bottom: 2px; }

  .thumb { top: 445px; width: 135px; height: 90px; background: var(--white); padding: 6px; box-shadow: 0 1px 4px rgba(0,0,0,.25); }
  .thumb div { width: 100%; height: 100%; }
  .thumb-1 { left: 64px; } .thumb-1 div { background: linear-gradient(180deg, #a9bfd8 0%, #8aa26a 55%, #5f7d3a 100%); }
  .thumb-2 { left: 211px; } .thumb-2 div { background: linear-gradient(180deg, #8a6a40 0%, #4a4a4a 45%, #2a2a2a 100%); }
  .thumb-3 { left: 359px; } .thumb-3 div { background: linear-gradient(180deg, #f0efe9 0%, #8ea070 55%, #8a5a38 100%); }

  .portrait-frame { left: 585px; top: 87px; width: 167px; height: 185px; border: 1.5px solid #e4d5b4; background: var(--white); padding: 5px 6px; }
  .portrait-frame div { width: 100%; height: 100%; background: linear-gradient(180deg, #c8c8c8 0%, #b4b4b4 100%); }

  .about { left: 586px; top: 287px; width: 172px; font-size: 9.2px; line-height: 15.7px; color: var(--ink); }
  .about h3 { font-style: italic; font-weight: 700; font-size: 9.2px; }

  .panel {
    left: 530px; top: 489px; width: 287px; height: 587px;
    background: linear-gradient(90deg, var(--beige-dark) 0%, var(--beige) 10%);
    border-radius: 60px 0 22px 0;
  }
  .services-title { left: 69px; top: 568px; font-size: 15.5px; font-weight: 700; font-style: italic; }
  .services { left: 69px; top: 623px; list-style: none; font-size: 10.4px; line-height: 18.3px; }
  .services li { position: relative; padding-left: 12px; margin-bottom: 10.6px; }
  .services li::before { content: ""; position: absolute; left: 2px; top: 8px; width: 3px; height: 3px; border-radius: 50%; background: var(--ink); }

  .questions { left: 69px; top: 975px; font-size: 8.6px; font-style: italic; color: var(--ink); }
  .partner { left: 84px; top: 1001px; display: flex; align-items: center; gap: 6px; }
  .partner-mark { width: 12px; height: 12px; border-radius: 50%; background: var(--band); }
  .partner-name { font-size: 13px; font-weight: 600; color: var(--ink); }
  .partner-text { left: 205px; top: 1004px; font-size: 10px; font-weight: 700; font-style: italic; }

  .advice-title { left: 550px; top: 568px; width: 250px; font-size: 15.5px; font-weight: 700; font-style: italic; line-height: 19px; }
  .advice { left: 550px; top: 621px; width: 228px; font-size: 10.2px; line-height: 18.3px; color: #2a2a2a; }
  .advice h4 { font-size: 9.4px; font-style: italic; font-weight: 700; color: var(--ink); }
  .advice ul { list-style: none; }
  .advice li { position: relative; padding-left: 11px; margin-bottom: 18px; }
  .advice li::before { content: ""; position: absolute; left: 1px; top: 8px; width: 3px; height: 3px; border-radius: 50%; background: var(--ink); }

  .contact { top: 1091px; font-size: 9.4px; line-height: 12px; color: var(--ink); font-style: normal; }
  .contact-address { left: 66px; }
  .contact-web { left: 325px; line-height: 14.5px; }
  .contact-phone { left: 585px; line-height: 14.5px; }
  .contact-phone b { font-weight: 700; }
</style>
</head>
<body>
  <div class="abs footer-band"></div>
  <div class="abs main-sheet"></div>

  <div class="abs hero-photo" role="img" aria-label="Foto des Abschiedsraums mit Urnenregal, Holztisch, Stühlen und Kerzen"></div>
  <div class="abs hero-fade"></div>

  <svg class="abs logo-shape" width="560" height="170" viewBox="0 0 560 170" aria-hidden="true">
    <path d="M0 0 H360 C350 90 250 160 110 165 C60 167 25 160 0 153 Z" fill="#ffffff"/>
  </svg>
  <div class="abs logo-dot"></div>
  <div class="abs logo-name">Bestattungshaus Lindmark</div>

  <h1 class="abs title-band"><span>Bestattungen Angehörige von</span><br><span>Verstorbenen</span></h1>

  <div class="abs thumb thumb-1"><div role="img" aria-label="Foto eines Bestattungsfahrzeugs vor Landschaft"></div></div>
  <div class="abs thumb thumb-2"><div role="img" aria-label="Foto einer Mappe mit Kerzen im Hintergrund"></div></div>
  <div class="abs thumb thumb-3"><div role="img" aria-label="Foto einer Dekoration mit Gräsern und Herz"></div></div>

  <div class="abs portrait-frame"><div role="img" aria-label="Porträtfoto des Bestatters"></div></div>

  <div class="abs about">
    <h3>Über mich :</h3>
    <p>Mein Name ist Wolfgang Brenner, ich kann auf eine langjährige Berufserfahrung als Humanbestatter zurückblicken.</p>
    <p>Die Versorgung und Bestattung eines Verstobenen, ist für Angehörige ein sehr wichtiger Aspekt.</p>
    <p>Daher habe ich es mir zur Aufgabe gemacht, Sie auf diesem Weg in Ruhe und mit Genauigkeit zu begleiten.</p>
  </div>

  <div class="abs panel"></div>

  <h2 class="abs services-title">Gerne übernehmen wir für Sie folgende Aufgaben:</h2>
  <ul class="abs services">
    <li>Persönliche Beratung und Betreuung Überführung im In- und Ausland</li>
    <li>Erledigung sämtlicher Formalitäten (z.B. Todesbescheinigung, Sterbeurkunde.)</li>
    <li>Versorgung des Verstorbenen nach DIN EN 15017</li>
    <li>Aufbahrung &amp; Abschiednahme in unseren Räumlichkeiten.</li>
    <li>Trauerdrucksachen ,Traueranzeigen<br>Beratung bei der Wahl der Bestattungsform und des Ortes der Beisetzung.</li>
    <li>Alle Bestattungsformen und Grab Arten sind bei uns möglich</li>
    <li>Terminabsprachen mit Pfarrer/Trauerrednern, Friedhofsverwaltung</li>
    <li>Individuelle Gestaltung, Organisation und Betreuung der Trauer Planung und</li>
    <li>Durchführung von Trauermusik oder auch die Bestellung eines Organisten</li>
    <li>Bestattungsvorsorge /Bestattungstreuhand</li>
  </ul>

  <p class="abs questions">Bei allen weiteren Fragen sprechen Sie uns an Wir sind gern für Sie da.</p>
  <div class="abs partner"><span class="partner-mark"></span><span class="partner-name">Waldruh</span></div>
  <p class="abs partner-text">Wir sind Partner von Waldruh.</p>

  <h2 class="abs advice-title">Was Sie im Trauerfall beachten müssen:</h2>
  <div class="abs advice">
    <h4>Bitte Bewahren Sie ruhe.</h4>
    <ul>
      <li>Jeder Trauerfall erfordert gewisse Maßnahmen die man treffen muss da diese im Bestattungsgesetzt Festgehalten sind.</li>
      <li>Bitte informieren Sie uns Zeitnah um alles wichtige vorab zu besprechen und den Ablauf der Überführung des Verstorbenen zu klären.</li>
    </ul>
    <h4>Verstirb ein Mensch zuhause</h4>
    <ul>
      <li>Müssen Sie zunächst den Hausarzt, Hausärztlichenvertretungsdienst <b>(116 117 )</b>, oder den Rettungsdienst <b>( 112 )</b> informieren. Dieser wird dann nach der ersten Leichenschau den Totenschein ausstellen, der für den weiteren Ablauf mit uns sehr wichtig ist.</li>
      <li>Tritt der Tod jedoch im Krankenhaus, Pflege &amp; Altenheim ein kümmert sich die dortige Verwaltung um die Formalitäten.</li>
    </ul>
  </div>

  <address class="abs contact contact-address">Bestattungshaus Lindmark<br>Ahornsteig 7<br>61462 Tannbach</address>
  <p class="abs contact contact-web">www.bestattungshaus-lindmark.de<br>info@bestattungshaus-lindmark.de</p>
  <p class="abs contact contact-phone">Tel:&nbsp;&nbsp;&nbsp;&nbsp;&nbsp; <b>06173 / 4820517</b><br>Mobil: <b>0152 / 83740162 24</b> Std Erreichbarkeit</p>
</body>
</html>
```